We need a card and logo design for a new business based in Dallas Texas called Ashgrove Financial LLC.

We provide bridge loans.We offer pay day loans,title loans and check cashing.Our products are emmergency loans that help borrowers meet short term liquidity needs until the next pay check.

The final design should communicate,professionalism,Sophistication and friendliness to our customers.Use the color Blue as much as possible and another eye catching color if possible.We will consider a profesional looking knight logo with the color Blue in it.Please design a full corporate identity.

```html
<!DOCTYPE html>
<html lang="en">
<head>
<meta charset="utf-8">
<title>Ashgrove Financial LLC — Business Cards</title>
<link rel="stylesheet" href="https://fonts.googleapis.com/css2?family=Roboto+Slab:wght@300;400;500&display=swap">
<style>
  :root {
    --page-bg: #eeeae3;
    --card-white: #ffffff;
    --blue-light: #0aa3d3;
    --blue-mid: #0787b8;
    --blue-deep: #0e5f93;
    --navy: #1d3a8a;
    --text-light: #ffffff;
    --shadow: rgba(40, 40, 40, 0.22);
  }
  * { box-sizing: border-box; margin: 0; padding: 0; }
  html, body {
    width: 1200px; height: 1200px; overflow: hidden;
    background: var(--page-bg);
    font-family: "Roboto Slab", Georgia, serif;
  }
  .stage {
    position: relative; width: 1200px; height: 1200px;
  }
  .card {
    position: absolute; left: 180px;
    width: 840px; height: 480px;
    box-shadow: 0 14px 30px var(--shadow);
    overflow: hidden;
  }
  /* Contact side */
  .card--contact {
    top: 90px;
    background: linear-gradient(180deg, var(--blue-light) 0%, var(--blue-mid) 55%, var(--blue-deep) 100%);
  }
  .card__white-band {
    position: absolute; left: 0; top: 0; width: 100%; height: 188px;
    background: var(--card-white);
  }
  .brand {
    position: absolute; display: flex; align-items: center; gap: 14px;
    color: var(--navy); font-weight: 400; white-space: nowrap;
  }
  .brand__dot {
    border-radius: 50%; background: var(--navy); flex: none;
  }
  .brand--small { left: 50%; top: 94px; transform: translate(-50%, -50%); font-size: 26px; }
  .brand--small .brand__dot { width: 22px; height: 22px; }
  .person {
    position: absolute; left: 318px; top: 214px;
    color: var(--text-light); font-size: 17px; line-height: 1.35;
  }
  .person__name { text-transform: uppercase; letter-spacing: 0.04em; }
  .contact {
    position: absolute; right: 40px; top: 214px; text-align: right;
    color: var(--text-light); font-size: 17px; line-height: 1.35;
  }
  .address {
    position: absolute; left: 44px; bottom: 44px;
    color: var(--text-light); font-size: 27px; line-height: 1.35;
  }
  /* Brand side */
  .card--brand {
    top: 630px;
    background: linear-gradient(180deg, var(--blue-light) 0%, var(--blue-mid) 50%, var(--blue-deep) 100%);
  }
  .brand--large { left: 50%; top: 50%; transform: translate(-50%, -50%); font-size: 46px; gap: 20px; }
  .brand--large .brand__dot { width: 34px; height: 34px; }
</style>
</head>
<body>
<main class="stage">
  <section class="card card--contact" aria-label="Business card, contact side">
    <div class="card__white-band"></div>
    <div class="brand brand--small">
      <span class="brand__dot"></span>
      <span class="brand__name">Ashgrove Financial LLC</span>
    </div>
    <div class="person">
      <p class="person__name">Daniel R Moore</p>
      <p class="person__title">Managing Director</p>
    </div>
    <div class="contact">
      <p>(t) 214-555-0148; fax (t) 214-555-0162</p>
      <p>danielrmoore@mail.com</p>
    </div>
    <address class="address" style="font-style:normal">
      <p>4180 Elm Grove Road</p>
      <p>Dallas, TX, 75201</p>
    </address>
  </section>

  <section class="card card--brand" aria-label="Business card, brand side">
    <div class="brand brand--large">
      <span class="brand__dot"></span>
      <span class="brand__name">Ashgrove Financial LLC</span>
    </div>
  </section>
</main>
</body>
</html>
```